Redesign existing website

We would like a redesign of the website http://www.velbrisanalytics.com that creates a more modern, up to date look.

Velbris Analytics creates software for social science research and is focused on making the software user friendly and easy to use. We would like to convey seriousness, but also
a very up to date, just released look.

Feel free to modify the logo if you wish.

Target Market(s)

Academics, researchers

Industry/Entity Type

Software

Requirements
Must have
• The design should incorporate the same information as the current website.

```html
<!DOCTYPE html>
<html lang="en">
<head>
<meta charset="utf-8">
<title>Velbris Analytics</title>
<link rel="stylesheet" href="https://fonts.googleapis.com/css2?family=Roboto+Condensed:wght@400;700&family=Saira+Condensed:wght@500;600&family=Raleway:wght@100&display=swap">
<style>
:root{
  --bg-top:#262626;
  --bg-header:#323232;
  --bg-hero:#0c0c0c;
  --bg-band:#3a3a3a;
  --bg-main:#363636;
  --bg-panel:#2a2a2a;
  --bg-footer:#2e2e2e;
  --line:#555;
  --text:#d8d8d8;
  --muted:#9a9a9a;
  --link:#3f63c8;
  --brand:#2a44a8;
  --yellow:#f5d000;
  --cream:#f5e6a8;
  --green:#7bc21e;
  --grey-bar:#8a9298;
}
*{margin:0;padding:0;box-sizing:border-box}
html,body{width:1200px;height:1175px;overflow:hidden}
body{position:relative;background:var(--bg-main);color:var(--text);font-family:"Roboto Condensed",Arial,sans-serif}
.abs{position:absolute}
a{color:inherit;text-decoration:none}

.top-bar{left:0;top:0;width:1200px;height:40px;background:var(--bg-top);border-bottom:1px solid #111}
.account-links{right:120px;top:11px;font-size:12px;color:#eee;display:flex;gap:14px}
.account-links span.sep{color:#888}

.site-header{left:0;top:41px;width:1200px;height:173px;background:linear-gradient(#353535,#2d2d2d)}
.brand-mark{left:171px;top:16px;width:72px;height:72px;border-radius:50%;background:var(--brand);border:4px solid #eee}
.brand-name{left:122px;top:96px;font-size:21px;font-weight:700;color:#e8e8e8;letter-spacing:.5px}
.tagline{left:122px;top:130px;font-size:14px;color:#eee;letter-spacing:.3px}
.main-nav{left:494px;top:23px;display:flex;font-size:12px;color:#999}
.main-nav a{padding:0 17px;border-left:1px solid #777}
.main-nav a:first-child{padding-left:0;border-left:0;color:#fff}
.preview-box{left:876px;top:2px;width:204px;height:62px;background:#1f1f1f;border-radius:0 0 8px 8px;box-shadow:0 3px 8px #000;text-align:center;padding-top:10px}
.preview-box .small{font-size:11px;color:var(--yellow)}
.preview-box .big{font-family:"Saira Condensed",sans-serif;font-size:19px;color:#444;text-shadow:0 1px 0 #777;letter-spacing:.5px;line-height:22px}

.hero{left:0;top:214px;width:1200px;height:368px;background:var(--bg-hero);border-top:1px solid #555}
.hero-chart{left:0;top:0}
.hero-copy{left:774px;top:74px;font-family:"Saira Condensed",sans-serif}
.hero-copy .lead{font-size:26px;color:#fff;line-height:28px;font-weight:500}
.hero-copy .focus{font-size:52px;color:var(--yellow);line-height:58px;font-weight:600}
.hero-copy .role{font-size:30px;color:var(--cream);line-height:30px;font-weight:500}

.band{left:0;top:582px;width:1200px;height:36px;background:var(--bg-band);border-top:1px solid #555;border-bottom:1px solid #222}

.welcome-title{left:122px;top:636px;font-family:"Raleway",sans-serif;font-weight:100;font-size:44px;color:#eee;letter-spacing:1px}
.mission{left:121px;top:703px;width:960px;font-size:12.3px;line-height:14px;color:#ddd}
.helps{left:121px;top:773px;font-size:12.3px;color:#ddd}
.benefits{left:120px;top:801px;width:960px;height:142px;background:var(--bg-panel);border-radius:8px}
.benefit{left:30px;font-size:12.5px;color:#ddd;display:flex;align-items:center;gap:22px}
.benefit i{display:block;width:22px;height:20px;border-radius:3px}
.download-btn{left:737px;top:830px;width:322px;height:77px;background:linear-gradient(#2a2a2a,#111);border:1px solid #777;border-radius:10px;box-shadow:0 2px 6px #000;display:flex;align-items:center;padding-left:38px;gap:12px;font-size:17px;color:#eee}
.download-btn b{color:#6d86e8;font-weight:400}

.site-footer{left:0;top:956px;width:1200px;height:182px;background:var(--bg-footer);border-top:1px solid #555}
.foot-mark{left:210px;top:14px;width:72px;height:72px;border-radius:50%;background:var(--brand);border:4px solid #eee}
.foot-name{left:160px;top:92px;font-size:21px;font-weight:700;color:#ddd}
.copyright{left:122px;top:125px;width:290px;font-size:11px;color:#888;text-align:center;line-height:13px}
.copyright p+p{margin-top:5px}
.foot-col{top:20px;font-size:11px;color:var(--link)}
.foot-col h3{font-size:12px;font-weight:400;color:#eee;margin-bottom:12px}
.foot-col li{list-style:none;height:24px;display:flex;align-items:flex-start;gap:8px}
.foot-col li i{display:block;width:16px;height:16px;border-radius:2px;background:#777}
.divider{top:22px;width:1px;height:144px;background:#111;border-right:1px solid #444}
.bottom-band{left:0;top:1138px;width:1200px;height:37px;background:#262626;border-top:1px solid #555}
</style>
</head>
<body>

<div class="abs top-bar">
  <nav class="abs account-links"><a href="#">Login</a><span class="sep">|</span><a href="#">Register</a></nav>
</div>

<header class="abs site-header">
  <div class="abs brand-mark"></div>
  <div class="abs brand-name">Velbris Analytics</div>
  <div class="abs tagline">Empowering the social science researcher</div>
  <nav class="abs main-nav">
    <a href="#">Home</a><a href="#">Products</a><a href="#">News</a><a href="#">About Us</a><a href="#">Contact Us</a>
  </nav>
  <a class="abs preview-box" href="#">
    <div class="small">Download Preview Release</div>
    <div class="big">VELBRIS DATA MANAGER</div>
  </a>
</header>

<section class="abs hero">
  <svg class="abs hero-chart" width="1200" height="368" viewBox="0 0 1200 368" style="overflow:visible">
    <defs>
      <linearGradient id="barGrey" x1="0" x2="1"><stop offset="0" stop-color="#6c7479"/><stop offset=".5" stop-color="#a9b0b5"/><stop offset="1" stop-color="#6c7479"/></linearGradient>
      <linearGradient id="barGreen" x1="0" x2="1"><stop offset="0" stop-color="#5a9c10"/><stop offset=".5" stop-color="#93d43a"/><stop offset="1" stop-color="#5a9c10"/></linearGradient>
      <linearGradient id="penRed" x1="0" x2="1"><stop offset="0" stop-color="#b01010"/><stop offset=".4" stop-color="#f03030"/><stop offset="1" stop-color="#a00c0c"/></linearGradient>
    </defs>
    <g stroke="#777" stroke-dasharray="5 3" stroke-width="1">
      <line x1="160" y1="15" x2="1075" y2="15"/><line x1="160" y1="75" x2="1075" y2="75"/>
      <line x1="160" y1="135" x2="1075" y2="135"/><line x1="160" y1="195" x2="1075" y2="195"/>
      <line x1="160" y1="254" x2="1075" y2="254"/><line x1="160" y1="314" x2="1075" y2="314"/>
    </g>
    <line x1="157.5" y1="0" x2="157.5" y2="368" stroke="#666"/>
    <g fill="#eee" font-family="Roboto Condensed, sans-serif" font-size="16">
      <text x="122" y="20">6%</text><text x="122" y="80">5%</text><text x="122" y="140">4%</text>
      <text x="122" y="200">3%</text><text x="122" y="259">2%</text><text x="122" y="319">1%</text>
    </g>
    <rect x="190" y="112" width="41" height="256" fill="url(#barGrey)"/>
    <rect x="277" y="268" width="41" height="100" fill="url(#barGreen)"/>
    <rect x="363" y="118" width="39" height="250" fill="url(#barGrey)"/>
    <rect x="448" y="64" width="42" height="304" fill="url(#barGrey)"/>
    <g role="img" aria-label="Red ballpoint pen standing in as a chart bar">
      <rect x="520" y="91" width="60" height="277" rx="6" fill="url(#penRed)"/>
    </g>
    <rect x="622" y="136" width="40" height="232" fill="url(#barGrey)"/>
    <rect x="707" y="-37" width="40" height="405" fill="url(#barGreen)"/>
  </svg>
  <div class="abs hero-copy">
    <div class="lead">Increasing The Power And<br>Efficiency Of Empirical</div>
    <div class="focus">Social Science</div>
    <div class="role">RESEARCHER</div>
  </div>
</section>

<div class="abs band"></div>

<main>
  <h1 class="abs welcome-title">WELCOME</h1>
  <p class="abs mission">The mission of Velbris Analytics, Inc. is to produce software products that multiply the power and efficiency of empirical scientific research in the social sciences. A central goal is to expand access to complex data sources and to the advanced methods of scientific investigation needed to analyze them. Reliance on antiquated data management tools imposes heavy costs on the research community. The VDM reduces the costs of research by allowing analysts to manipulate data without the assistance of professional programming staff.</p>
  <p class="abs helps">The Velbris Data Manager (VDM) helps researchers:</p>
  <section class="abs benefits">
    <div class="abs benefit" style="top:12px"><i style="background:#d9a93a"></i>Integrate data from different periods, places, and sources</div>
    <div class="abs benefit" style="top:45px"><i style="background:linear-gradient(90deg,#5a8fe0 33%,#8fc83a 33% 66%,#e0b43a 66%)"></i>Restructure complex data structures for analysis</div>
    <div class="abs benefit" style="top:78px"><i style="background:#3f8fd0;border-radius:50%"></i>Generate simple descriptive statistics for diagnostic purposes and feasibility analyses</div>
    <div class="abs benefit" style="top:110px"><i style="background:#eee"></i>Export subsets of variables and cases in formats suitable for analysis in any statistical package.</div>
  </section>
  <a class="abs download-btn" href="#">
    <svg width="24" height="32" viewBox="0 0 24 32"><rect x="7" y="0" width="10" height="16" fill="#2d6fe0"/><path d="M0 14h24L12 32z" fill="#2d6fe0"/></svg>
    <span>Download <b>Velbris Data Manager</b></span>
  </a>
</main>

<footer class="abs site-footer">
  <div class="abs foot-mark"></div>
  <div class="abs foot-name">Velbris Analytics</div>
  <div class="abs copyright"><p>Copyright © Velbris Analytics 2011. All Rights Reserved.</p><p>Increasing The Power And Efficiency Of Empirical<br>Social Science Research</p></div>

  <div class="abs divider" style="left:456px"></div>
  <div class="abs divider" style="left:655px"></div>
  <div class="abs divider" style="left:858px"></div>

  <div class="abs foot-col" style="left:529px"><h3>SITE LINKS</h3><ul>
    <li>Home</li><li>Products</li><li>News</li><li>About Us</li><li>Contact Us</li></ul></div>
  <div class="abs foot-col" style="left:732px"><h3>PRODUCTS</h3><ul>
    <li>Overview</li><li>Features</li><li>Datasets</li><li>Screenshots</li><li>Support</li></ul></div>
  <div class="abs foot-col" style="left:932px"><h3>CONNECT WITH US</h3><ul>
    <li><i style="background:#4aa8d8"></i>Chatter</li><li><i style="background:#3b5a9a"></i>Friendbook</li>
    <li><i style="background:#c8c8c8"></i>VidStream</li><li><i style="background:#e8821e"></i>Rss Feed</li>
    <li><i style="background:#cfd8e8"></i>Email</li></ul></div>
</footer>
<div class="abs bottom-band"></div>

</body>
</html>
```